Flyer informing about the activities of people in action

Wege im Wandel (www.wegeimwandel-beispiel.ch) offers coaching, medation, support for traumatized people and conflict and crisis intervention. The flyer should inform about the activities in a plain and simple way (see logo on the homepage).

Target Market(s)

Adults who live in Switzerland or Germany

Requirements
Must have
• - simple flyer, the design is based on my logo. Brief information about my offer, reference to my homepage www.wegeimwandel-beispiel.
- 2-sided: on the first page - fire circle with text (see homepage - Home), on the back - offer with logo
- possibly a square flyer

Should not have
• no photos

```html
<!DOCTYPE html>
<html lang="de">
<head>
<meta charset="utf-8">
<title>Wege im Wandel – Flyer</title>
<link href="https://fonts.googleapis.com/css2?family=Arimo:wght@400;700&display=swap" rel="stylesheet">
<style>
  :root{
    --gold:#b08d55;
    --gold-dark:#9c7a45;
    --gold-light:#c9a76c;
    --green:#085e52;
    --navy:#2a3a85;
    --ink:#111111;
    --paper:#ffffff;
    --backdrop:#e6e6e6;
    --grey-soft:#cfcbca;
  }
  *{margin:0;padding:0;box-sizing:border-box}
  html,body{width:1200px;height:1200px;overflow:hidden}
  body{background:var(--backdrop);font-family:"Arimo",Arial,sans-serif;position:relative;color:var(--ink)}
  .flyer{position:absolute;background:var(--paper);overflow:hidden;box-shadow:0 10px 24px rgba(0,0,0,.18)}
  .flyer--front{left:45px;top:249px;width:527px;height:677px}
  .flyer--back{left:620px;top:242px;width:532px;height:684px}
  .abs{position:absolute}
  .center{left:0;right:0;text-align:center}

  .front__header{position:absolute;left:0;top:0;width:527px;height:420px}
  .logo-disc{position:absolute;left:139px;top:-76px;width:238px;height:238px;border-radius:50%;background:var(--paper);display:flex;align-items:flex-end;justify-content:center;padding-bottom:62px}
  .logo-name{font-size:24px;font-weight:400;color:var(--green);display:flex;align-items:center;gap:8px}
  .logo-name::before{content:"";width:14px;height:14px;border-radius:50%;background:var(--gold)}
  .hero-title{color:#fff;font-weight:700;font-size:30px}
  .hero-text{color:#fff;font-size:14px;line-height:18px}
  .photo{left:25px;top:430px;width:191px;height:178px;border:1.5px solid var(--green);background:linear-gradient(160deg,#f4f4f4 0%,#e9e6e2 55%,#8a7a6a 100%)}
  .intro{left:253px;top:427px;width:270px;color:var(--green);font-size:20px;line-height:22px}
  .label{color:var(--navy);font-size:14px;line-height:16px}
  .fine{font-size:8.6px;line-height:11px;color:var(--ink);width:280px}
  .footer{position:absolute;left:0;right:0;bottom:0;background:var(--green);color:#fff;display:flex;align-items:center;justify-content:center;font-size:14px;letter-spacing:1.4px}
  .flyer--front .footer{height:52px;padding-right:28px}
  .flyer--back .footer{height:54px;padding-right:30px}

  .gold-cap{position:absolute;left:139px;top:-135px;width:236px;height:236px;border-radius:50%;background:linear-gradient(160deg,var(--gold-light),var(--gold-dark))}
  .back__lead{font-size:19px;color:var(--green)}
  .back__lead strong{display:block;font-size:20px;margin-top:4px}
  .service{position:absolute;left:30px;right:30px;text-align:center}
  .service h2{font-size:19px;font-weight:700;margin-bottom:14px}
  .service .summary{font-size:9.6px;font-weight:700;line-height:12px;margin-bottom:9px}
  .service .questions{font-size:9.6px;line-height:12.2px}
  .service--coaching h2{color:var(--gold)}
  .service--mediation h2{color:var(--green)}
  .service--trauma h2{color:var(--navy)}
  .divider{position:absolute;left:45px;width:455px;height:1px;background:var(--gold)}
  .back__texture{position:absolute;left:0;right:0;top:466px;height:170px;background:linear-gradient(180deg,#fff 0%,#efedec 45%,var(--grey-soft) 100%)}
</style>
</head>
<body>

<section class="flyer flyer--front">
  <svg class="front__header" viewBox="0 0 527 420" role="img" aria-label="Goldene Fläche mit Facettenmuster und geschwungenem grünem Rand">
    <defs>
      <linearGradient id="goldFacet" x1="0" y1="0" x2="1" y2="1">
        <stop offset="0" stop-color="#b8945c"/>
        <stop offset=".5" stop-color="#a8854f"/>
        <stop offset="1" stop-color="#9b7944"/>
      </linearGradient>
    </defs>
    <path d="M0 0H527V335Q300 445 0 372Z" fill="var(--green)"/>
    <path d="M0 0H527V330Q300 420 0 352Z" fill="url(#goldFacet)"/>
  </svg>

  <div class="logo-disc"><span class="logo-name">Wege im Wandel</span></div>

  <h1 class="abs center hero-title" style="top:178px">Sie Möchten</h1>
  <p class="abs center hero-text" style="top:223px">Ihre belastende Situation lösen.Ihre wichtigen Fragen klären.</p>
  <h1 class="abs center hero-title" style="top:252px">Leichter Weiterkommen</h1>
  <p class="abs center hero-text" style="top:299px">in der frustrierenden Zusammenarbeit oder Ihrem mühsamen<br>(Zusammen-)Leben.</p>

  <div class="abs photo" role="img" aria-label="Porträtfoto der Beraterin"></div>

  <p class="abs intro">Weil die eigene Not die Denk-, Fühl - und Handlungsfähigkeit vermindert, lohnt sich eine Begleitung.</p>
  <p class="abs label" style="left:235px;top:521px">In meinem Berufsalltag bin ich</p>
  <p class="abs fine" style="left:235px;top:540px">Casemanagerin, Coach, Begleiterin von traumatisierten Menschen, Mediatorin, Dozentin, Juristin</p>
  <p class="abs label" style="left:231px;top:566px">Meine Freizeit gestalte ich als</p>
  <p class="abs fine" style="left:231px;top:587px">Menschenliebhaberin, Köchin, Bergsteigerin, Skitourenfahrerin, Schwimmerin, Weltenbummlerin</p>

  <footer class="footer">www.wegeimwandel-beispiel.ch</footer>
</section>

<section class="flyer flyer--back">
  <div class="gold-cap" role="img" aria-label="Goldener Halbkreis mit Facettenmuster"></div>
  <div class="back__texture" role="img" aria-label="Sanfter grauer Facettenhintergrund"></div>

  <p class="abs center back__lead" style="top:124px">Ich begleite Sie und bringe Ihnen<strong>Orientierung, Klarheit und Unterstützung</strong></p>

  <article class="service service--coaching" style="top:198px">
    <h2>Coaching</h2>
    <p class="summary">Manchmal braucht man ein Gegenüber zum Klären der eigenen Situation oder beim Entdecken neuer Sichtweisen und Handlungsmöglichkeiten.</p>
    <p class="questions">Mögliche Fragen: Wo stehen Sie heute und wo wollen Sie hin? Nutzen Sie Ihre Handlungsspielräume und Ihre Fähigkeiten? Was macht Sie glücklich?</p>
  </article>
  <div class="divider" style="top:314px"></div>

  <article class="service service--mediation" style="top:337px">
    <h2>Mediation</h2>
    <p class="summary">Gewisse Konflikte können Sie nicht mehr selber lösen. Wenige Worte entzünden einen erbitterten Streit oder erzeugen eisige Stille.</p>
    <p class="questions">Mögliche Fragen: Wie finden Sie Gehör? Sehen Sie die Sichtweise Ihres Gegenübers? Wie finden Sie etwas vom verlorenen Vertrauen wieder? Wie kommen Sie wieder ins Gespräch um gemeinsam nötige Lösungen zu finden?</p>
  </article>
  <div class="divider" style="top:464px"></div>

  <article class="service service--trauma" style="top:483px">
    <h2>Begleitung von traumatisierten Menschen</h2>
    <p class="summary">Ihr Leben fühlt sich oft schwer, bedrückend und freudlos an. Erfolglos haben Sie probiert, sich von dieser Kontakt- und Perspektivlosigkeit zu befreien.</p>
    <p class="questions">In dieser Begleitung geht es vorerst darum einen sicheren Rahmen zu schaffen, in dem Kontakt möglich wird und später gehalten werden kann.</p>
  </article>

  <footer class="footer">www.wegeimwandel-beispiel.ch</footer>
</section>

</body>
</html>
```